Gas utility and appliance store needs awesome web design

The Flint Hearth is a South African based brick and mortar shop looking to improve it's on-line presence.
We cover the whole gambit or products, appliances, information, services, installations and utility related to domestic gas (in SA still considered an alternative fuel) with our most important offerings being the sale of the gas (LPG) itself in combination with high end kitchen and household gas based appliances (stoves, cookers, heaters, fireplaces etc)
Wesite needs to portray our professional (been in the market since 47), family owned (3'rd gen now) roots - it should create the impression of a market leader - and must also portray our domestic (read man in the street) focus and practical approach.
Something professional but light-hearted enough for the general public.
Design must reinforce the belief that LPG is a green,safe and affordable fuel option for domestic use

Target Market(s)

upper middle class market 25-70

Industry/Entity Type

Appliance

Requirements
Must have
• landing page
our company
sustainability
contact us page
menu bar with links to pages (shop, specific information etc)

```html
<!DOCTYPE html>
<html lang="en">
<head>
<meta charset="utf-8">
<title>The Flint Hearth</title>
<link rel="stylesheet" href="https://fonts.googleapis.com/css2?family=Arimo:wght@400;700&family=Poiret+One&display=swap">
<style>
:root{
  --topbar:#3f3f3f;
  --blue:#1c8fd6;
  --ink:#333;
  --body:#555;
  --muted:#777;
  --rule:#d4d4d4;
  --footer:#454545;
  --footer-rule:#5e5e5e;
  --footer-text:#b9b9b9;
  --crumb:#f3f3f3;
}
*{box-sizing:border-box;margin:0;padding:0}
html,body{width:965px;height:1200px;overflow:hidden;background:#fff}
body{position:relative;font-family:"Arimo",Arial,sans-serif;color:var(--body)}
.abs{position:absolute}
ul{list-style:none}

.topbar{left:0;top:0;width:965px;height:30px;background:var(--topbar);font-size:8px;color:#eee}
.topbar span{position:absolute;top:11px}
.topbar .inquiry{left:144px;color:var(--blue)}
.search{left:648px;top:7px;width:173px;height:18px;background:#fff;border-radius:3px}
.search svg{position:absolute;right:5px;top:3px}

.brand{left:149px;top:55px;display:flex;align-items:center;gap:6px}
.brand .dot{width:11px;height:11px;border-radius:50%;background:var(--blue)}
.brand .name{font-weight:700;font-size:15px;color:var(--blue)}

.nav{left:490px;top:73px;display:flex;font-size:9.5px;color:#444}
.nav a{padding:6px 11px;text-decoration:none;color:inherit}
.nav a.active{background:#333;color:#fff;border-radius:2px}

.hero{left:143px;top:110px;width:679px;height:262px;background:linear-gradient(180deg,#fff 0%,#f2f6ea 45%,#b9d37a 75%,#7fa942 100%)}
.hero-shadow{left:70px;top:370px;width:825px;height:22px;background:radial-gradient(ellipse at top,rgba(0,0,0,.18),transparent 70%)}
.hero-title{left:390px;top:212px;font-family:"Poiret One",sans-serif;font-size:26px;color:#444;letter-spacing:.5px}
.hero-brand{left:740px;top:180px;font-weight:700;font-size:12px;color:var(--blue);width:72px;text-align:center}

.intro{left:144px;top:396px;width:680px;font-family:"Poiret One",sans-serif;font-size:23.5px;line-height:28px;color:#555}
.divider{left:143px;top:503px;width:679px;height:1px;background:var(--rule)}

.label{top:540px;font-size:7.5px;font-weight:700;color:#333;text-transform:uppercase}
.label.right{left:742px;display:flex;align-items:center;gap:3px}
.circle-arrow{width:10px;height:10px;border-radius:50%;background:var(--blue);display:inline-block;position:relative}
.circle-arrow::after{content:"";position:absolute;left:3px;top:3px;border:2px solid #fff;border-width:0 1.5px 1.5px 0;width:3px;height:3px;transform:rotate(-45deg)}

.card{top:553px;width:216px;height:220px;border:1px solid #d8d8d8;border-radius:3px;padding:4px}
.card .media{height:102px;width:100%}
.card h3{margin:6px 2px 0;font-size:9.5px;font-weight:700;color:#333;text-transform:uppercase;letter-spacing:.4px;line-height:13px}
.card p{margin:4px 2px 0;font-size:8px;line-height:14.5px;color:#666}
.card .meta{position:absolute;left:6px;right:6px;bottom:7px;display:flex;justify-content:space-between;font-size:7.5px;font-weight:700;color:#444}
.card .meta span{display:flex;align-items:center;gap:3px}
.card .meta i{width:10px;height:10px;border-radius:50%;background:var(--blue);display:inline-block}
.media.brand-tile{display:flex;align-items:center;justify-content:center;gap:8px;background:#fff}
.media.brand-tile .name{font-weight:700;font-size:20px;color:var(--blue)}
.media.brand-tile .dot{width:14px;height:14px;border-radius:50%;background:var(--blue)}

.feature{top:810px;width:158px;border-top:1px solid var(--rule);padding-top:10px;font-size:8.2px;line-height:16.3px;color:#666}
.feature .icon{float:left;width:27px;height:27px;border-radius:50%;background:#333;margin:0 8px 4px 0;display:flex;align-items:center;justify-content:center}

.crumbbar{left:0;top:957px;width:965px;height:28px;background:var(--crumb);border-top:1px solid #ddd}
.crumbs{left:143px;top:966px;font-size:7.5px;color:#888;display:flex;align-items:center;gap:5px}
.crumbs .globe{width:12px;height:12px;border-radius:50%;background:#999}
.crumbs b{font-weight:400;color:#555}
.social{left:746px;top:965px;display:flex;gap:4px}
.social i{width:12px;height:12px;border-radius:2px;display:block}

.footer{left:0;top:985px;width:965px;height:215px;background:var(--footer)}
.fcol{top:990px;width:116px;font-size:8.8px;color:var(--footer-text)}
.fcol h4{font-size:8.8px;font-weight:700;color:#eee;padding-bottom:5px;border-bottom:1px solid var(--footer-rule)}
.fcol li{padding:5px 0 5px 7px;border-bottom:1px solid var(--footer-rule);position:relative;line-height:11px}
.fcol li::before{content:"";position:absolute;left:1px;top:9px;border-left:3px solid #aaa;border-top:2px solid transparent;border-bottom:2px solid transparent}
.contact{left:663px;top:990px;width:160px;font-size:8.8px;color:#eee;line-height:16.2px}
.contact h4{font-size:8.8px;font-weight:700;border-bottom:1px solid var(--footer-rule);padding-bottom:5px;margin-bottom:4px;line-height:11px}
.copyright{left:143px;top:1183px;font-size:7px;color:#aaa}
.top-link{left:800px;top:1183px;font-size:7px;color:#aaa}
.footer-rule{left:0;top:1174px;width:965px;height:1px;background:#3a3a3a}
</style>
</head>
<body>

<header>
  <div class="abs topbar">
    <span class="inquiry">Send an inquiry</span>
    <span style="left:216px">Phone: 555 - 304172586</span>
    <span style="left:319px">info@flinthearth.example</span>
  </div>
  <div class="abs search">
    <svg width="12" height="12" viewBox="0 0 12 12"><circle cx="5" cy="5" r="3.6" fill="none" stroke="#222" stroke-width="1.6"/><line x1="7.6" y1="7.6" x2="11" y2="11" stroke="#222" stroke-width="2"/></svg>
  </div>
  <div class="abs brand"><span class="name">The Flint Hearth</span><span class="dot"></span></div>
  <nav class="abs nav">
    <a class="active" href="#">Home</a><a href="#">Our Company</a><a href="#">Sustainability</a><a href="#">Products</a><a href="#">Contact</a>
  </nav>
</header>

<section>
  <div class="abs hero-shadow"></div>
  <div class="abs hero" role="img" aria-label="Smiling woman in a green meadow beside a gas cylinder, a kettle barbecue and a gas stove"></div>
  <div class="abs hero-title">We Make Gas Hotter</div>
  <div class="abs hero-brand">The Flint Hearth</div>
</section>

<p class="abs intro">Hello! We are the Third Generation of The Flint Hearth. Over 47 years of experience in the LP Gas industry ensures that you are in good hands at The Flint Hearth.... Afterall we make GAS Hot!</p>
<div class="abs divider"></div>

<div class="abs label" style="left:143px">Our Company:</div>
<div class="abs label right">Send an inquiry <span class="circle-arrow"></span></div>

<article class="abs card" style="left:143px">
  <div class="media brand-tile"><span class="name">The Flint Hearth</span><span class="dot"></span></div>
  <h3>Over 65 years of making lives better</h3>
  <p>Lorem ipsum dolor sit amet, consectetur adipisicing elit, sed do eiusmod tempor incididunt ut labolore magna aliqua. Ut enim ad minim veniam.</p>
  <div class="meta"><span><i></i>Web Design, Webworks</span><span>Dec. 03. 09 <i></i></span></div>
</article>
<article class="abs card" style="left:374px">
  <div class="media" role="img" aria-label="Gas cylinder, barbecue and stove on a grassy background" style="background:linear-gradient(180deg,#eef3e2,#9cc45a)"></div>
  <h3>Our Products - Your total gas solution</h3>
  <p>Lorem ipsum dolor sit amet, consectetur adipisicing elit, sed do eiusmod tempor incididunt ut labolore magna aliqua. Ut enim ad minim veniam.</p>
  <div class="meta"><span><i></i>Web Design, Webworks</span><span>Dec. 03. 09 <i></i></span></div>
</article>
<article class="abs card" style="left:605px">
  <div class="media" role="img" aria-label="Laughing child holding a daisy in a green field" style="background:linear-gradient(135deg,#6f9a3a,#b8d27a 55%,#e9dccb)"></div>
  <h3>LPG - A greener, safer &amp; affordable fuel</h3>
  <p>Lorem ipsum dolor sit amet, consectetur adipisicing elit, sed do eiusmod tempor incididunt ut labolore magna aliqua. Ut enim ad minim veniam.</p>
  <div class="meta"><span><i></i>Web Design, Webworks</span><span>Dec. 03. 09 <i></i></span></div>
</article>

<div class="abs feature" style="left:143px">
  <span class="icon"><svg width="15" height="15" viewBox="0 0 24 24"><path fill="#fff" d="M12 2l3 7h7l-5.6 4.3 2.1 7.2L12 16.3 5.5 20.5l2.1-7.2L2 9h7z"/></svg></span>
  Lorem ipsum dolor sit amet, consectetur adipisicing elit, sed do eiusmod tempor incididunt ut labore et dolore magna aliqua. Ut enim ad minim veniam, quis nostrud exercitation ullamco laboris nisi ut aliquip ex ea commodo conse.
</div>
<div class="abs feature" style="left:316px">
  <span class="icon"><svg width="15" height="12" viewBox="0 0 16 12"><rect x="0.5" y="0.5" width="15" height="11" rx="1.5" fill="#fff"/><path d="M1 1l7 6 7-6" stroke="#333" stroke-width="1.5" fill="none"/></svg></span>
  Consectetur adipisicing elit, sed do eiusmod tempor incididunt ut labore et dolore im veniam.<br>quis nostrud exercitation ullamco laboris nisi ut aliquip ex ea commodo cem ipsum dolor sit amet.
</div>
<div class="abs feature" style="left:490px">
  <span class="icon"><svg width="14" height="13" viewBox="0 0 14 13"><rect x="1" y="7" width="3" height="6" fill="#fff"/><rect x="5.5" y="4" width="3" height="9" fill="#fff"/><rect x="10" y="1" width="3" height="12" fill="#fff"/></svg></span>
  Lorem ipsum dolor sit amet, consectetur adipisicing elit, sed do eiusmod tempor incididunt ut labore et dolore magna aliqua. Ut enim ad minim veniam, quis nostrud exercitation ullamco laboris nisi ut aliquip ex ea commodo conse.
</div>
<div class="abs feature" style="left:663px">
  <span class="icon"><svg width="15" height="14" viewBox="0 0 15 14"><rect x="0.5" y="0.5" width="14" height="9.5" rx="1" fill="#fff"/><rect x="5.5" y="10" width="4" height="2" fill="#fff"/><rect x="3.5" y="12" width="8" height="1.5" fill="#fff"/></svg></span>
  Ut enim ad minim veniam, quis nostrud exercitation ullamco laboris nisi ut aliquip ex ea commodo conse. Lorem ipsum dolor sit amet.<br>Sed do eiusmod tempor incididunt ut labore et dolore magna aliqua.
</div>

<div class="abs crumbbar"></div>
<div class="abs crumbs"><span class="globe"></span>Home &rsaquo; About &rsaquo; <b>Over 65 years of making lives better</b></div>
<div class="abs social">
  <i style="background:#e8792b"></i><i style="background:#3b5a9a"></i><i style="background:#3aaee0"></i><i style="background:#d7d7d7"></i><i style="background:#2fa8e0"></i>
</div>

<footer>
  <div class="abs footer"></div>
  <div class="abs fcol" style="left:143px"><h4>Latest News</h4><ul><li>Our New Page is online</li><li>Example</li><li>Example</li><li>Example</li></ul></div>
  <div class="abs fcol" style="left:273px"><h4>Pages</h4><ul><li>Home</li><li>About</li><li>Company Info</li><li>Sustainability</li><li>Products</li><li>Contact Us</li></ul></div>
  <div class="abs fcol" style="left:404px"><h4>Key Products</h4><ul><li>LPG</li><li>BBQ</li><li>Build-in Hobs</li><li>Build-in Ovens</li><li>Coffee Machine</li><li>Extractor Hoods</li><li>Heaters</li></ul></div>
  <div class="abs fcol" style="left:533px"><h4>Miscellaneous</h4><ul><li>Subscribe for News Letter</li><li>Terms of Service</li><li>Site Map</li></ul></div>
  <div class="abs contact">
    <h4>Contact Information</h4>
    P.O. Box 41209<br>Rosewood Vale 0217<br>South Africa<br>Ph: 00 - 000- 00000<br>Fax: 00 - 000 - 00000
    <div style="margin-top:9px">We're available from 9 AM- 5 PM.</div>
  </div>
  <div class="abs footer-rule"></div>
  <div class="abs copyright">All content Copyright © 2010 Northvale Studio</div>
  <div class="abs top-link">top &#8963;</div>
</footer>

</body>
</html>
```